Tour operator needs simple coded WordPress site (updated extra payment for coding and guaranteed)

[update 9/7/2015]
If you design a new logo and it gets accepted, even if we use another template with your logo you will get $50
[update 8/7/2015]
Update on questions about dual-language
For dual languages we are happy to set up a second site with the same designs in a second language.
For the design aspect just allow the user to switch between languages with an icon.
For the coding, a replica of the site on a second server will do (to save messing around with multiple language plugins) - we will populate it with Chinese text
[original post]
Simple coded WordPress site for tours
You can choose to design only or design and code ($340 design, $150 bonus for coding)
Open design brief - use your creativity
Will be in 2 languages (English and Chinese) but design needs only to be in one language
Winning design will be chosen only from home page, but the winner must make a second standard template page when chosen at no extra cost.
Must be responsive design
We only need homepage and standard template page design and coding, we will populate the pages
You can use design ideas from our pamphlet if you like - attached
Only a sample logo and colors on website and pamphlet - feel free to change as the current ones seem restrictive
Current website framework only to give an idea of the number of pages and basic menu structure (no need to use existing navigation style or any style at all for that matter, open brief)
http://brightwattlejourneys.com.au/
Target Market(s)
Chinese parents of kids 10-14 (the kids will take the tour)
Industry/Entity Type
Tour
Number of Pages Required
2 page
Look and feel
Each slider illustrates characteristics of the customer's brand and the style your logo design should communicate.

```html
<!DOCTYPE html>
<html lang="en">
<head>
<meta charset="utf-8">
<title>Bright Wattle Journeys</title>
<link href="https://fonts.googleapis.com/css2?family=Oswald:wght@400;500&family=Lato:wght@400;700&display=swap" rel="stylesheet">
<style>
:root{
  --orange:#f5a51f;
  --orange-soft:#fcd085;
  --blue:#17b6d3;
  --blue-bright:#2fd0ee;
  --green:#86a86a;
  --green-soft:#a9c691;
  --green-text:#7da35c;
  --header-green:#8fae74;
  --ink:#3a3a3a;
  --body-text:#555;
  --film:#111;
  --gallery-bg:#f1f1f1;
  --footer:#3b3b3b;
  --footer-base:#2a2a2a;
  --footer-text:#d9d9d9;
}
*{margin:0;padding:0;box-sizing:border-box}
html,body{width:1200px;height:2406px;overflow:hidden}
body{position:relative;background:#fff;font-family:'Lato',sans-serif;color:var(--body-text)}
.abs{position:absolute}

/* header */
.top-band{left:0;top:0;width:1200px;height:112px;background:linear-gradient(180deg,#99b87e,var(--header-green))}
.brand{left:40px;top:10px;width:302px;height:212px;background:#fff;box-shadow:0 3px 10px rgba(0,0,0,.35);z-index:5;display:flex;align-items:center;justify-content:center;gap:14px;padding:0 18px}
.brand-dot{width:34px;height:34px;border-radius:50%;background:var(--orange);flex:none}
.brand-name{font-family:'Oswald',sans-serif;font-weight:500;font-size:36px;line-height:1.1;color:var(--orange);text-transform:uppercase}
.lang{top:21px;width:22px;height:16px;border-radius:2px}
.lang.en{left:903px;background:#2a4b9a}
.lang.zh{left:935px;background:#d8261d}
.social-top{top:14px;width:30px;height:30px;border-radius:50%;background:#fff}
.main-nav{left:481px;top:59px;width:719px;height:46px;background:var(--orange);display:flex;align-items:center;justify-content:space-around;padding:0 16px 0 30px}
.main-nav a{font-family:'Oswald',sans-serif;font-size:19px;color:#fff;text-decoration:none;text-transform:uppercase}

/* film strip hero */
.film{left:0;top:109px;width:1200px;height:465px;background:var(--film)}
.hero-shot{top:32px;height:401px}
.shot-harbour{left:0;width:385px;background:linear-gradient(180deg,#c9a9d9 0%,#a98fcf 40%,#5a5aa0 70%,#2f3a7a 100%)}
.shot-family{left:406px;width:385px;background:linear-gradient(160deg,#7a1f1f 0%,#c33a3a 45%,#d9a48a 70%,#b52a2a 100%)}
.shot-sunset{left:813px;width:387px;background:linear-gradient(180deg,#2c1510 0%,#c6421b 45%,#f08c22 70%,#2a0d05 100%)}
.hero-line{left:850px;top:66px;width:330px;font-family:'Oswald',sans-serif;font-size:41px;line-height:1.1;color:#fff}
.badge{left:1076px;top:494px;width:112px;height:112px;border-radius:50%;background:#fff;border:5px solid #888;z-index:4}

/* section headings */
.section-title{left:0;width:1200px;text-align:center;font-family:'Oswald',sans-serif;font-size:33px;font-weight:400;color:var(--orange)}
.section-title span{color:var(--blue)}
.title-rule{left:520px;width:160px;height:2px;background:linear-gradient(90deg,transparent,#ddd,transparent)}

/* about */
.about-lead{left:60px;top:690px;width:1080px;text-align:center;font-size:16.5px;font-weight:700;color:var(--green-text);line-height:1.45}
.about-copy{left:70px;top:746px;width:1060px;text-align:center;font-size:12.6px;line-height:1.6;color:#666}

.feature{top:877px;width:340px;height:411px;padding:112px 26px 0 30px;color:#fff}
.feature.safe{left:53px;background:var(--orange)}
.feature.learn{left:430px;background:var(--blue)}
.feature.includes{left:807px;background:var(--green)}
.feature-tab{position:absolute;left:-8px;top:21px;width:300px;height:60px;font-family:'Oswald',sans-serif;font-size:22px;color:#333;text-transform:uppercase;padding:17px 0 0 38px;transform:rotate(2deg);box-shadow:0 2px 4px rgba(0,0,0,.15)}
.safe .feature-tab{background:var(--orange-soft)}
.learn .feature-tab{background:var(--blue-bright)}
.includes .feature-tab{background:var(--green-soft)}
.feature ul{list-style:none}
.feature li{position:relative;padding-left:24px;font-size:13.6px;line-height:1.32;margin-bottom:14px}
.includes li{margin-bottom:15px}
.feature li::before{content:"";position:absolute;left:2px;top:3px;width:5px;height:9px;border-right:2px solid #fff;border-bottom:2px solid #fff;transform:rotate(45deg)}

.shadow-rule{left:100px;top:1330px;width:1000px;height:10px;background:radial-gradient(ellipse at center,rgba(0,0,0,.12),transparent 70%)}

/* tours */
.tour-photo{top:1453px;width:249px;height:186px;border:4px solid #fff;box-shadow:0 1px 5px rgba(0,0,0,.3)}
.photo-college{left:54px;background:linear-gradient(180deg,#3b7fd4 0%,#8ab7e8 35%,#8a6a45 60%,#4e7a2e 100%)}
.photo-capital{left:638px;background:linear-gradient(180deg,#4a8ad8 0%,#9cc4ee 40%,#8a6b46 65%,#3a4f6a 100%)}
.tour-info{top:1452px;width:230px}
.tour-info h3{font-family:'Lato',sans-serif;font-weight:700;font-size:16px;color:var(--green-text);text-transform:uppercase;padding-bottom:10px;border-bottom:1px solid #ddd;letter-spacing:.3px}
.tour-time{font-size:12.5px;color:var(--orange);margin:14px 0 10px}
.tour-text{font-size:12.6px;line-height:1.55;color:#555}
.read-more{display:inline-block;margin-top:13px;background:var(--blue);color:#fff;font-size:13px;padding:7px 12px;border-radius:3px}
.dots{left:561px;top:1689px;display:flex;gap:7px}
.dots i{width:11px;height:11px;border-radius:50%;background:#ddd;display:block}
.dots i.on{background:var(--orange)}

/* gallery */
.gallery-band{left:0;top:1748px;width:1200px;height:356px;background:var(--gallery-bg)}
.gallery-shot{top:1872px;width:217px;height:154px}
.g1{left:133px;background:linear-gradient(180deg,#e9a04a,#c46a24 60%,#5a3216)}
.g2{left:372px;background:linear-gradient(180deg,#6aaee4,#9bc6e4 45%,#6b7a6a 65%,#2e6f9e)}
.g3{left:611px;background:linear-gradient(180deg,#3a7ad0,#9cc0ea 50%,#eef2f6 70%,#3a6f9c)}
.g4{left:850px;background:linear-gradient(180deg,#c9cdd2,#e8c84a 35%,#d1b08a 60%,#4a4a6a)}
.gallery-cap{top:2043px;width:217px;text-align:center;font-size:13.6px;color:#333}
.g-arrow{top:1936px;width:28px;height:28px;border-radius:50%;border:2px solid #c8c8c8}
.g-arrow svg{display:block}

/* footer */
.site-footer{left:0;top:2104px;width:1200px;height:264px;background:var(--footer)}
.footer-base{left:0;top:2368px;width:1200px;height:38px;background:var(--footer-base);text-align:center;font-size:11.5px;color:#cfcfcf;line-height:38px}
.f-col{top:2148px;color:var(--footer-text)}
.f-col h4{font-family:'Lato',sans-serif;font-weight:700;font-size:16px;color:#fff;padding-bottom:7px;border-bottom:1px solid #555;width:214px;margin-bottom:12px}
.f-divider{top:2148px;width:1px;height:185px;background:#555}
.quick{left:53px}
.quick li{list-style:none;font-size:12.6px;margin-bottom:14px;position:relative;padding-left:14px}
.quick li::before{content:"";position:absolute;left:0;top:4px;border-left:5px solid #ddd;border-top:4px solid transparent;border-bottom:4px solid transparent}
.newsletter{left:321px}
.newsletter p{font-size:12.2px;line-height:1.5;width:220px;margin-bottom:10px}
.field{width:213px;height:25px;background:#e6e6e6;color:#444;font-size:12px;padding:5px 8px;margin-bottom:12px}
.subscribe{display:inline-block;background:var(--orange);color:#fff;font-size:12px;padding:6px 11px}
.contact{left:635px}
.contact-row{display:flex;gap:16px;align-items:flex-start;font-size:12.2px;line-height:1.5;margin-bottom:14px;width:240px}
.contact-row strong{font-size:15px;color:#fff;font-weight:700}
.follow{left:962px}
.follow-row{display:flex;align-items:center;gap:20px;font-size:12.2px;margin-bottom:12px}
.follow-row span.sq{width:27px;height:27px;background:#5a5a5a;display:block}
</style>
</head>
<body>

<header>
  <div class="abs top-band"></div>
  <div class="abs brand"><span class="brand-dot"></span><span class="brand-name">Bright Wattle Journeys</span></div>
  <span class="abs lang en" aria-label="English"></span>
  <span class="abs lang zh" aria-label="Chinese"></span>
  <span class="abs social-top" style="left:1002px"></span>
  <span class="abs social-top" style="left:1040px"></span>
  <span class="abs social-top" style="left:1079px"></span>
  <span class="abs social-top" style="left:1117px"></span>
  <nav class="abs main-nav">
    <a href="#">Home</a><a href="#">About Us</a><a href="#">Tours</a><a href="#">Programs</a><a href="#">Blog</a><a href="#">Contact Us</a>
  </nav>
</header>

<section class="abs film">
  <svg class="abs" style="left:0;top:0" width="1200" height="465" aria-hidden="true">
    <defs>
      <pattern id="sprockets" x="6" y="0" width="35" height="32" patternUnits="userSpaceOnUse">
        <rect x="6" y="8" width="17" height="17" rx="3" fill="#fff"/>
      </pattern>
    </defs>
    <rect x="0" y="0" width="1200" height="32" fill="url(#sprockets)"/>
    <rect x="0" y="433" width="1200" height="32" fill="url(#sprockets)"/>
  </svg>
  <div class="abs hero-shot shot-harbour" role="img" aria-label="Harbour city skyline with opera house and arch bridge at dusk"></div>
  <div class="abs hero-shot shot-family" role="img" aria-label="Smiling mother and child"></div>
  <div class="abs hero-shot shot-sunset" role="img" aria-label="Kangaroo silhouettes against an outback sunset">
    <p class="abs hero-line" style="left:37px;top:66px">Educational, safe, culturally enlightening and fun.</p>
  </div>
</section>
<div class="abs badge"></div>

<main>
  <h2 class="abs section-title" style="top:610px">ABOUT <span>US</span></h2>
  <div class="abs title-rule" style="top:662px"></div>
  <p class="abs about-lead">At the Bright Wattle Journeys we are passionate about educational travel and opportunities for students to gain academic and cultural understanding of Australia.</p>
  <p class="abs about-copy">14 day premium cultural and educational tours to Australian cities. Educational, safe, culturally enlightening and fun. Learn about educational institutions, history, sports, laws and customs, food and culture whileimproving your English. At the Bright Wattle Journeys we are passionate about educational travel and providing opportunities for students to learn more about a country and gain a deeper understanding of the culture. The out of classroom experience gained on our trips is invaluable. Planning and leading an the Bright Wattle Journeys tour is easy because our team of dedicated experts assists every step of the way – from meticulously planning the curriculum to planning every detail of your trip, to accompanying you on tour.</p>

  <article class="abs feature safe">
    <h3 class="feature-tab">Safe and Secure</h3>
    <ul>
      <li>Staff certified by the government for Working With Children</li>
      <li>Staff certified in first aid care</li>
      <li>Professional accommodation with excellent history in caring for children with extremely well documented Safety Management Procedures including;</li>
      <li>Safety Management - reducing risk when taking students out of the classroom</li>
      <li>Safety &amp; Emergency Procedures (Location-specific)</li>
      <li>Standard Operating Procedures</li>
    </ul>
  </article>
  <article class="abs feature learn">
    <h3 class="feature-tab">Educational and Cultural</h3>
    <ul>
      <li>Professional lecturers from Sydney universities</li>
      <li>2 hour lessons every day in easy to understand, high-quality English</li>
      <li>Subjects from the Australian Educational Curriculum as well as cultural information on Australia</li>
      <li>How to live, get around, shop and socialise in Australia</li>
      <li>Attitudes to languages, food, religion and culture</li>
      <li>Outdoor activities and sport</li>
    </ul>
  </article>
  <article class="abs feature includes">
    <h3 class="feature-tab">Includes</h3>
    <ul>
      <li>Return tickets</li>
      <li>Visa fees</li>
      <li>Travel accident insurance</li>
      <li>Accommodation</li>
      <li>Meals (breakfast, lunch and dinner)</li>
      <li>Transportation</li>
      <li>Courses and Lectures</li>
      <li>Guides</li>
      <li>Entry tickets and travel expenses</li>
    </ul>
  </article>

  <div class="abs shadow-rule"></div>

  <h2 class="abs section-title" style="top:1372px">OUR <span>TOURS</span></h2>
  <div class="abs title-rule" style="top:1424px"></div>

  <div class="abs tour-photo photo-college" role="img" aria-label="Sandstone college building with lawn"></div>
  <div class="abs tour-info" style="left:329px">
    <h3>Harbour College</h3>
    <p class="tour-time">12:00 – 17:00</p>
    <p class="tour-text">At vero eos et accusamus et dignissimos ducimus qui blanditiis praes voluptatum deleniti atque corrupti quos dolore quas molest excepturi sint occaecati</p>
    <span class="read-more">Read More</span>
  </div>
  <div class="abs tour-photo photo-capital" role="img" aria-label="Historic parliament building with clock tower by a river"></div>
  <div class="abs tour-info" style="left:913px">
    <h3>Capital Hall</h3>
    <p class="tour-time">12:00 – 17:00</p>
    <p class="tour-text">At vero eos et accusamus et dignissimos ducimus qui blanditiis praes voluptatum deleniti atque corrupti quos dolore quas molest excepturi sint occaecati</p>
    <span class="read-more">Read More</span>
  </div>
  <div class="abs dots"><i class="on"></i><i></i><i></i><i></i><i></i></div>

  <div class="abs gallery-band"></div>
  <h2 class="abs section-title" style="top:1786px">OUR <span>GALLERY</span></h2>
  <div class="abs title-rule" style="top:1838px"></div>
  <span class="abs g-arrow" style="left:50px"><svg width="24" height="24"><path d="M14 7l-5 5 5 5" fill="none" stroke="#c8c8c8" stroke-width="2"/></svg></span>
  <span class="abs g-arrow" style="left:1118px"><svg width="24" height="24"><path d="M10 7l5 5-5 5" fill="none" stroke="#c8c8c8" stroke-width="2"/></svg></span>
  <div class="abs gallery-shot g1" role="img" aria-label="Kangaroo leaping at sunset"></div>
  <div class="abs gallery-shot g2" role="img" aria-label="City harbour skyline with bridge"></div>
  <div class="abs gallery-shot g3" role="img" aria-label="Opera house sails on the water"></div>
  <div class="abs gallery-shot g4" role="img" aria-label="Group of students in yellow caps"></div>
  <p class="abs gallery-cap" style="left:133px">Qui Blanditiis Praes</p>
  <p class="abs gallery-cap" style="left:372px">Deleniti Atque Corrupti</p>
  <p class="abs gallery-cap" style="left:611px">Blanditiis Praes Voluptatum</p>
  <p class="abs gallery-cap" style="left:850px">Excepturi Sint Occaecati</p>
</main>

<footer>
  <div class="abs site-footer"></div>
  <div class="abs f-divider" style="left:273px"></div>
  <div class="abs f-divider" style="left:589px"></div>
  <div class="abs f-divider" style="left:914px"></div>

  <div class="abs f-col quick">
    <h4 style="width:180px">Quick Links</h4>
    <ul><li>Home</li><li>About Us</li><li>Tours</li><li>Programs</li><li>Contact</li></ul>
  </div>
  <div class="abs f-col newsletter">
    <h4>Newsletter</h4>
    <p>Signup with us and get update in your inbox.</p>
    <div class="field">Your Name</div>
    <div class="field">Email address</div>
    <span class="subscribe">Subscribe</span>
  </div>
  <div class="abs f-col contact">
    <h4 style="width:240px">Contact Us</h4>
    <div class="contact-row"><svg width="14" height="20" viewBox="0 0 14 20"><path d="M7 0a7 7 0 0 0-7 7c0 5 7 13 7 13s7-8 7-13a7 7 0 0 0-7-7zm0 10a3 3 0 1 1 0-6 3 3 0 0 1 0 6z" fill="#fff"/></svg><span>At vero eos et accusa dignissimos ducimus qui blanditiis praes</span></div>
    <div class="contact-row"><svg width="16" height="16" viewBox="0 0 16 16"><path d="M3 1l3 3-2 2c1 2 3 4 6 6l2-2 3 3-2 2C7 15 1 9 1 3z" fill="#fff"/></svg><strong>1-800-555-0142</strong></div>
    <div class="contact-row"><svg width="16" height="16" viewBox="0 0 16 16"><rect x="4" y="1" width="8" height="4" fill="#fff"/><rect x="1" y="5" width="14" height="7" rx="1" fill="#fff"/><rect x="4" y="10" width="8" height="5" fill="#fff" stroke="#3b3b3b"/></svg><strong>02-5550-1987</strong></div>
  </div>
  <div class="abs f-col follow">
    <h4 style="width:190px">Follow Us On</h4>
    <div class="follow-row"><span class="sq"></span>Friendsy</div>
    <div class="follow-row"><span class="sq"></span>Chirpline</div>
    <div class="follow-row"><span class="sq"></span>Clipcast</div>
    <div class="follow-row"><span class="sq"></span>Workwire</div>
  </div>

  <div class="abs footer-base">© 2015 Bright Wattle Journeys. All Rights Reserved</div>
</footer>

</body>
</html>
```